Business Card Design Project

Business Card
We are rebranding with a new logo
Industry/Entity Type
Business
Contact Information for Business Card
Dennis Marlow +61 427581962 dennis@qovo.com.au P.O. Box 872 Kelvindale QLD 4309
Requirements
Must have
- Logo

```html
<!DOCTYPE html>
<html lang="en">
<head>
<meta charset="utf-8">
<title>Qovo International – Business Card</title>
<link rel="stylesheet" href="https://fonts.googleapis.com/css2?family=Roboto:wght@400;500;700&display=swap">
<style>
  :root {
    --backdrop: #3b3b3b;
    --card: #ffffff;
    --map-tint: #eef0f2;
    --brand-blue: #1c9ad8;
    --text-grey: #5f6265;
    --rule-grey: #c9cbcd;
    --accent-orange: #f07f22;
    --band-deep: #0c4a72;
    --band-mid: #10628f;
    --band-bright: #08a8e6;
  }
  * { margin: 0; padding: 0; box-sizing: border-box; }
  html, body {
    width: 1200px;
    height: 1000px;
    overflow: hidden;
    background: var(--backdrop);
    font-family: "Roboto", Arial, sans-serif;
  }
  .business-card {
    position: absolute;
    left: 220px;
    top: 280px;
    width: 760px;
    height: 434px;
    background: var(--card);
    overflow: hidden;
  }
  .map-backdrop {
    position: absolute;
    left: 10px;
    top: 12px;
    width: 740px;
    height: 310px;
    background: radial-gradient(ellipse at center, var(--map-tint) 0%, rgba(238,240,242,0.4) 60%, rgba(255,255,255,0) 100%);
  }
  .brand-name {
    position: absolute;
    left: 110px;
    top: 112px;
    width: 240px;
    text-align: center;
    color: var(--brand-blue);
    font-weight: 700;
    line-height: 1;
  }
  .brand-name .brand-main {
    display: block;
    font-size: 64px;
    letter-spacing: 1px;
  }
  .brand-name .brand-sub {
    display: block;
    margin-top: 14px;
    font-size: 20px;
    letter-spacing: 3px;
  }
  .divider {
    position: absolute;
    left: 379px;
    top: 87px;
    width: 1px;
    height: 153px;
    background: var(--rule-grey);
  }
  .contact-block {
    position: absolute;
    left: 415px;
    top: 83px;
  }
  .person-name {
    color: var(--brand-blue);
    font-weight: 500;
    font-size: 27px;
    letter-spacing: 0.5px;
    line-height: 32px;
  }
  .postal-address {
    margin-top: 22px;
    color: var(--text-grey);
    font-size: 16.5px;
    line-height: 20px;
  }
  .contact-list {
    list-style: none;
    margin-top: 14px;
  }
  .contact-list li {
    display: flex;
    align-items: center;
    color: var(--text-grey);
    font-size: 16.5px;
    line-height: 24.5px;
  }
  .contact-list svg {
    width: 13px;
    height: 13px;
    margin-right: 5px;
    flex: none;
  }
  .footer-band {
    position: absolute;
    left: 0;
    bottom: 0;
    width: 760px;
    height: 100px;
    background: linear-gradient(90deg, var(--band-deep) 0%, var(--band-mid) 45%, var(--band-bright) 100%);
  }
</style>
</head>
<body>
  <div class="business-card">
    <div class="map-backdrop" role="img" aria-label="Faint light grey world map in the card background"></div>

    <div class="brand-name">
      <span class="brand-main">QOVO</span>
      <span class="brand-sub">INTERNATIONAL</span>
    </div>

    <div class="divider"></div>

    <div class="contact-block">
      <p class="person-name">DENNIS MARLOW</p>
      <p class="postal-address">P.O. Box 872 Kelvindale QLD 4309</p>
      <ul class="contact-list">
        <li>
          <svg viewBox="0 0 16 16" aria-hidden="true"><path fill="var(--accent-orange)" d="M3.6 1.5l2.3 2.6-1.4 1.7c.9 2 2.4 3.6 4.5 4.6l1.7-1.4 2.7 2.2-1.2 2.3C7.2 13.3 2.6 8.7 1.4 3z"/></svg>
          +61 427581962
        </li>
        <li>
          <svg viewBox="0 0 16 16" aria-hidden="true"><rect x="1" y="3" width="14" height="10" fill="var(--accent-orange)"/><path d="M1 3.5l7 5 7-5" stroke="#fff" stroke-width="1.4" fill="none"/></svg>
          dennis@qovo.com.au
        </li>
        <li>
          <svg viewBox="0 0 16 16" aria-hidden="true"><g fill="none" stroke="var(--accent-orange)" stroke-width="1.4"><circle cx="8" cy="8" r="6.5"/><ellipse cx="8" cy="8" rx="2.8" ry="6.5"/><path d="M1.5 8h13M2.5 4.8h11M2.5 11.2h11"/></g></svg>
          www.qovo.com.au
        </li>
      </ul>
    </div>

    <div class="footer-band" role="img" aria-label="Decorative orange and blue curved band along the bottom of the card"></div>
  </div>
</body>
</html>
```